Core Values Poster

I would like the layout I put together designed professionally. The poster will be vertical. I need two sizes 24" x 36" and 28" x 40". Convert the black and white poster into something colorful so that the icons pop and it is suitable for framing. The website is https://www.cedar4wellness.com/ for reference.

```html
<!DOCTYPE html>
<html lang="en">
<head>
<meta charset="utf-8">
<title>Cedar4 Wellness – Our Core Values Posters</title>
<link rel="stylesheet" href="https://fonts.googleapis.com/css2?family=Roboto:wght@500;700&family=Roboto+Condensed:wght@700&display=swap">
<style>
  :root {
    --backdrop: #8c8c8c;
    --paper: #ffffff;
    --gold: #b99a36;
    --banner-blue: #1a6fb8;
    --label-grey: #555555;
    --text-dark: #3a3a3a;
    --text-mid: #4a4a4a;
    --integrity: #29a3dc;
    --energy: #7cc142;
    --gratitude: #8e2a8b;
    --intelligence: #f7941d;
    --innovation: #e3232b;
  }
  * { box-sizing: border-box; margin: 0; padding: 0; }
  html, body { width: 1200px; height: 840px; overflow: hidden; }
  body {
    background: var(--backdrop);
    font-family: "Roboto", Arial, sans-serif;
    position: relative;
  }
  .poster {
    position: absolute;
    background: var(--paper);
  }
  .poster--small { left: 88px; top: 109px; width: 467px; height: 700px; }
  .poster--large { left: 567px; top: 31px; width: 545px; height: 778px; }

  .brand-name {
    position: absolute;
    width: 272px;
    text-align: center;
    font-family: "Roboto", Arial, sans-serif;
    font-weight: 500;
    font-size: 35px;
    letter-spacing: 1px;
    color: var(--gold);
    white-space: nowrap;
  }
  .poster--small .brand-name { left: 95px; top: 70px; }
  .poster--large .brand-name { left: 134px; top: 96px; }

  .title-banner {
    position: absolute;
    width: 270px;
    height: 35px;
    border: 4px solid #f4f4f4;
    border-radius: 3px;
    background: linear-gradient(90deg, #8f8f8f 0%, #b9b9b9 55%, #e6e6e6 100%);
    box-shadow: 2px 4px 6px rgba(0,0,0,.35);
    display: flex;
    align-items: center;
    justify-content: center;
    font-family: "Roboto Condensed", "Arial Narrow", sans-serif;
    font-weight: 700;
    font-size: 25px;
    color: var(--banner-blue);
  }
  .poster--small .title-banner { left: 95px; top: 163px; }
  .poster--large .title-banner { left: 134px; top: 182px; }

  .value {
    position: absolute;
    width: 146px;
    height: 146px;
    border-radius: 50%;
    border: 4px solid #f7f7f7;
    background: radial-gradient(circle at 45% 40%, #ffffff 0%, #eeeeee 45%, #bdbdbd 100%);
    box-shadow: 6px 8px 10px rgba(0,0,0,.45);
  }
  .value__icon {
    position: absolute;
    left: 50%;
    top: 12px;
    width: 66px;
    height: 66px;
    margin-left: -33px;
    border-radius: 50%;
  }
  .value__icon--integrity { background: radial-gradient(circle, #7fcdee 0%, var(--integrity) 70%); }
  .value__icon--energy { background: radial-gradient(circle, #b6e08e 0%, var(--energy) 70%); }
  .value__icon--gratitude { background: radial-gradient(circle, #c477c1 0%, var(--gratitude) 70%); }
  .value__icon--intelligence { background: radial-gradient(circle, #fbc37e 0%, var(--intelligence) 70%); }
  .value__icon--innovation { background: radial-gradient(circle, #f07a7f 0%, var(--innovation) 70%); }

  .value__name {
    position: absolute;
    left: 0; right: 0;
    top: 84px;
    text-align: center;
    font-weight: 700;
    font-size: 15px;
    letter-spacing: .3px;
    color: var(--text-dark);
  }
  .value__points {
    position: absolute;
    left: 0; right: 0;
    top: 103px;
    list-style: none;
    display: flex;
    flex-direction: column;
    align-items: center;
    font-weight: 500;
    font-size: 7.4px;
    line-height: 9px;
    color: var(--text-mid);
  }
  .value__points ul { list-style: none; }
  .value__points li::before { content: "• "; }

  .size-label {
    position: absolute;
    font-weight: 700;
    font-size: 25px;
    color: var(--label-grey);
  }
  .poster--small .size-label { right: 12px; top: 662px; }
  .poster--large .size-label { right: 20px; top: 740px; }
</style>
</head>
<body>

<section class="poster poster--small" aria-label="Core values poster, 24 by 36 inches">
  <div class="brand-name">Cedar4 Wellness</div>
  <div class="title-banner">Our Core Values</div>

  <article class="value" style="left:159px;top:210px">
    <div class="value__icon value__icon--integrity" role="img" aria-label="Handshake icon"></div>
    <h2 class="value__name">INTEGRITY</h2>
    <div class="value__points"><ul><li>Dependability</li><li>Honesty</li><li>Loyalty</li></ul></div>
  </article>
  <article class="value" style="left:0px;top:311px">
    <div class="value__icon value__icon--energy" role="img" aria-label="Lightning bolt icon"></div>
    <h2 class="value__name">ENERGY</h2>
    <div class="value__points"><ul><li>Body &amp; Mind</li><li>Be Proactive</li><li>It's Up to you</li></ul></div>
  </article>
  <article class="value" style="left:288px;top:317px">
    <div class="value__icon value__icon--gratitude" role="img" aria-label="Hands holding a heart icon"></div>
    <h2 class="value__name">GRATITUDE</h2>
    <div class="value__points"><ul><li>For Patients</li><li>For Coworkers</li><li>For Life</li></ul></div>
  </article>
  <article class="value" style="left:71px;top:471px">
    <div class="value__icon value__icon--intelligence" role="img" aria-label="Light bulb with brain icon"></div>
    <h2 class="value__name">INTELLIGENCE</h2>
    <div class="value__points"><ul><li>Know Your Duty</li><li>Continuous Learning</li><li>Always Ask</li></ul></div>
  </article>
  <article class="value" style="left:247px;top:474px">
    <div class="value__icon value__icon--innovation" role="img" aria-label="Balance scales icon"></div>
    <h2 class="value__name">INNOVATION</h2>
    <div class="value__points"><ul><li>Think Outside of the Box</li><li>Go Above &amp; Beyond</li><li>Develop New Skills</li></ul></div>
  </article>

  <div class="size-label">24" x 36"</div>
</section>

<section class="poster poster--large" aria-label="Core values poster, 28 by 40 inches">
  <div class="brand-name">Cedar4 Wellness</div>
  <div class="title-banner">Our Core Values</div>

  <article class="value" style="left:198px;top:249px">
    <div class="value__icon value__icon--integrity" role="img" aria-label="Handshake icon"></div>
    <h2 class="value__name">INTEGRITY</h2>
    <div class="value__points"><ul><li>Dependability</li><li>Honesty</li><li>Loyalty</li></ul></div>
  </article>
  <article class="value" style="left:58px;top:350px">
    <div class="value__icon value__icon--energy" role="img" aria-label="Lightning bolt icon"></div>
    <h2 class="value__name">ENERGY</h2>
    <div class="value__points"><ul><li>Body &amp; Mind</li><li>Be Proactive</li><li>It's Up to you</li></ul></div>
  </article>
  <article class="value" style="left:327px;top:355px">
    <div class="value__icon value__icon--gratitude" role="img" aria-label="Hands holding a heart icon"></div>
    <h2 class="value__name">GRATITUDE</h2>
    <div class="value__points"><ul><li>For Patients</li><li>For Coworkers</li><li>For Life</li></ul></div>
  </article>
  <article class="value" style="left:110px;top:509px">
    <div class="value__icon value__icon--intelligence" role="img" aria-label="Light bulb with brain icon"></div>
    <h2 class="value__name">INTELLIGENCE</h2>
    <div class="value__points"><ul><li>Know Your Duty</li><li>Continuous Learning</li><li>Always Ask</li></ul></div>
  </article>
  <article class="value" style="left:287px;top:512px">
    <div class="value__icon value__icon--innovation" role="img" aria-label="Balance scales icon"></div>
    <h2 class="value__name">INNOVATION</h2>
    <div class="value__points"><ul><li>Think Outside of the Box</li><li>Go Above &amp; Beyond</li><li>Develop New Skills</li></ul></div>
  </article>

  <div class="size-label">28" x 40"</div>
</section>

</body>
</html>
```